Building technology company seek stationery design and folder design

Letterhead, and a folder design
ideally, I would have two letter head design, one is for one-page bussiness letter. the other one I can use for longer document such report, or analysis regular report page
you can find company logo and overall style at our website:
www.quorvantelab.net

we are in building technology business, using internet of things technology to improve building energy efficiency to make building greener.

Industry/Entity Type

It Company

Requirements
Must have
• company logo
Nice to have
• techy look abstract graphics, etc.
Should not have
• no comment

```html
<!DOCTYPE html>
<html lang="en">
<head>
<meta charset="utf-8">
<title>Quorvante Lab Presentation Folder</title>
<link rel="stylesheet" href="https://fonts.googleapis.com/css2?family=Roboto:wght@400;500&display=swap">
<style>
  :root {
    --stage: #c9c9c9;
    --cover: #0b1f22;
    --cover-light: #12292c;
    --lime: #8dc63f;
    --lime-faint: #1f3a2a;
    --ink-light: #d9e0de;
  }
  * { margin: 0; padding: 0; box-sizing: border-box; }
  html, body {
    width: 1200px;
    height: 1090px;
    overflow: hidden;
    background: var(--stage);
    font-family: "Roboto", Arial, sans-serif;
  }
  .folder-spread {
    position: absolute;
    left: 50px;
    top: 165px;
    width: 1100px;
    height: 760px;
    display: flex;
  }
  .cover {
    position: relative;
    width: 550px;
    height: 100%;
    background: linear-gradient(160deg, var(--cover-light), var(--cover) 60%);
    border-top: 7px solid var(--lime);
    border-bottom: 7px solid var(--lime);
  }
  .cover--back { border-right: 1px solid #061315; }
  .cover--front { border-left: 1px solid #1b3336; }

  .back-watermark {
    position: absolute;
    left: 0;
    right: 0;
    top: 250px;
    text-align: center;
    font-weight: 500;
    font-size: 64px;
    letter-spacing: 2px;
    color: var(--lime-faint);
  }
  .back-contact {
    position: absolute;
    left: 0;
    right: 0;
    bottom: 34px;
    display: flex;
    justify-content: center;
    gap: 18px;
    font-size: 10px;
    color: var(--ink-light);
  }
  .contact-item { display: flex; align-items: center; gap: 5px; }
  .contact-item svg { width: 9px; height: 9px; fill: var(--lime); }

  .front-brand {
    position: absolute;
    left: 0;
    right: 0;
    top: 255px;
    display: flex;
    justify-content: center;
    align-items: center;
    gap: 14px;
  }
  .brand-mark {
    width: 30px;
    height: 30px;
    background: var(--lime);
  }
  .brand-name {
    font-weight: 500;
    font-size: 38px;
    letter-spacing: 3px;
    color: var(--lime);
  }
</style>
</head>
<body>
  <main class="folder-spread">
    <section class="cover cover--back">
      <div class="back-watermark">Quorvante Lab</div>
      <div class="back-contact">
        <span class="contact-item">
          <svg viewBox="0 0 10 10"><path d="M2 0.5 L3.8 2.6 L2.9 3.8 Q4 6 6.2 7.1 L7.4 6.2 L9.5 8 L8.2 9.5 Q3.5 9 0.5 1.8 Z"/></svg>
          (555) 014-2837
        </span>
        <span class="contact-item">
          <svg viewBox="0 0 10 10"><path d="M0 2 H10 V8 H0 Z M0.6 2.4 L5 5.6 L9.4 2.4" fill="var(--lime)"/></svg>
          info@quorvantelab.net
        </span>
        <span class="contact-item">
          <svg viewBox="0 0 10 10"><circle cx="5" cy="5" r="4.6"/></svg>
          www.quorvantelab.net
        </span>
      </div>
    </section>
    <section class="cover cover--front">
      <div class="front-brand">
        <span class="brand-mark"></span>
        <span class="brand-name">Quorvante Lab</span>
      </div>
    </section>
  </main>
</body>
</html>
```